Marrowby's Vacation Rentals Business Card

Multi Million dollar villa rentals in the Dominican Republic.

Industry/Entity Type

Business

Contact Information for Business Card

I am looking for a high-end look around my company name/logo (see attached) on one side incorporating the following info: first and last name, title, address, phone #, email and company website. On the backside I want to add a full color picture of one of our villas (see attached).

```html
<!DOCTYPE html>
<html lang="en">
<head>
<meta charset="utf-8">
<title>Marrowby's Vacation Rentals – Business Card</title>
<link rel="stylesheet" href="https://fonts.googleapis.com/css2?family=Open+Sans:wght@400;600&display=swap">
<style>
  :root {
    --stage: #1b1b1b;
    --card-white: #ffffff;
    --card-dark: #221f20;
    --ink: #1e1e1e;
    --rule: #2b2b2b;
    --orange: #f26722;
    --orange-light: #f7941d;
    --photo-sky: #8fa9b8;
    --photo-house: #d9d6cf;
    --photo-garden: #4e6b3a;
    --photo-pool: #2a86b8;
    --white: #ffffff;
  }
  * { margin: 0; padding: 0; box-sizing: border-box; }
  html, body {
    width: 1200px; height: 741px; overflow: hidden;
    background: var(--stage);
    font-family: "Open Sans", Arial, sans-serif;
  }
  .stage { position: relative; width: 1200px; height: 741px; }

  .card {
    position: absolute; top: 229px; height: 282px;
    box-shadow: 0 2px 6px rgba(0,0,0,.6);
    overflow: hidden;
  }
  .card--front { left: 100px; width: 495px; background: var(--card-white); }
  .card--back  { left: 606px; width: 493px; background: var(--card-dark); }

  /* front: brand */
  .brand {
    position: absolute; left: 24px; top: 27px;
    display: flex; align-items: center; gap: 9px;
  }
  .brand__dot { width: 34px; height: 34px; border-radius: 50%; background: var(--orange); }
  .brand__name {
    font-weight: 600; color: var(--ink);
    font-size: 20px; line-height: 23px;
  }

  /* front: contact */
  .contact {
    position: absolute; right: 23px; top: 26px; text-align: right; color: var(--ink);
  }
  .contact__name { font-weight: 600; color: var(--orange); font-size: 17px; line-height: 17px; }
  .contact__title { font-size: 13px; line-height: 14px; }
  .contact__list { list-style: none; margin-top: 8px; }
  .contact__item {
    display: flex; justify-content: flex-end; align-items: center; gap: 5px;
    font-size: 12.5px; line-height: 17px;
  }
  .contact__icon {
    width: 15px; height: 15px; background: var(--orange);
    display: flex; align-items: center; justify-content: center;
  }

  .rule { position: absolute; left: 0; width: 100%; background: var(--rule); }
  .rule--top { top: 106px; height: 5px; }
  .rule--bottom { top: 236px; height: 4px; }

  .villa-photo {
    position: absolute; left: 0; top: 115px; width: 100%; height: 121px;
    background: linear-gradient(180deg,
      var(--photo-sky) 0%, var(--photo-house) 18%, var(--photo-house) 55%,
      var(--photo-garden) 68%, var(--photo-house) 78%, var(--photo-pool) 88%, var(--photo-pool) 100%);
  }

  .address-band {
    position: absolute; left: 0; bottom: 0; width: 100%; height: 39px;
    background: linear-gradient(180deg, var(--orange-light), var(--orange));
    color: var(--white); font-size: 13px;
    display: flex; align-items: center; justify-content: center;
  }

  /* back */
  .web {
    position: absolute; right: 32px; top: 224px;
    color: var(--white); font-size: 17px;
  }
  .web__accent { color: var(--orange); }
</style>
</head>
<body>
<main class="stage">
  <section class="card card--front">
    <div class="brand">
      <span class="brand__dot"></span>
      <span class="brand__name">Marrowby's<br>Vacation Rentals</span>
    </div>

    <div class="contact">
      <p class="contact__name">Elena Varga</p>
      <p class="contact__title">Managing Director</p>
      <ul class="contact__list">
        <li class="contact__item">(0)809 555 0142
          <span class="contact__icon">
            <svg width="7" height="11" viewBox="0 0 7 11"><rect x="0.6" y="0.6" width="5.8" height="9.8" rx="1" fill="none" stroke="#fff" stroke-width="1.2"/><rect x="1.8" y="2" width="3.4" height="4.5" fill="#fff"/></svg>
          </span>
        </li>
        <li class="contact__item">Info@marrowbysmail.com
          <span class="contact__icon">
            <svg width="11" height="8" viewBox="0 0 11 8"><rect x="0.5" y="0.5" width="10" height="7" fill="none" stroke="#fff"/><path d="M0.5 0.5 L5.5 4.5 L10.5 0.5" fill="none" stroke="#fff"/></svg>
          </span>
        </li>
      </ul>
    </div>

    <div class="rule rule--top"></div>
    <div class="villa-photo" role="img" aria-label="Photograph of a white villa with arched veranda, blue loungers and a pool"></div>
    <div class="rule rule--bottom"></div>

    <p class="address-band">PO BOX 48 Playa Linda Road, Sosúa, Dominican Republic</p>
  </section>

  <section class="card card--back">
    <p class="web">Info@<span class="web__accent">marrowbysvillas</span>.com</p>
  </section>
</main>
</body>
</html>
```